Advertisement Design Project

Attached is the information I need in a big color ad

10X11 that will go in a weekly local paper.
I am open to color and graphics-no pictures of people please.

My logo is also attached, which I would like in the ad.

Sorry for the short notice-I just got a deal on the space and it is due Friday.

```html
<!DOCTYPE html>
<html lang="en">
<head>
<meta charset="utf-8">
<title>New Tax Laws – Estate Planning Workshop</title>
<link rel="stylesheet" href="https://fonts.googleapis.com/css2?family=Archivo+Black&family=Roboto+Condensed:ital,wght@0,400;0,700;1,700&display=swap">
<style>
  :root {
    --page: #ffffff;
    --ad-bg: #2a2522;
    --white: #ffffff;
    --gold: #f5c000;
    --cream: #f6ef8c;
    --grey-text: #8a8580;
    --photo-dark: #1e2320;
    --photo-mid: #4d5a52;
    --photo-light: #c9cdc4;
  }
  * { margin: 0; padding: 0; box-sizing: border-box; }
  html, body {
    width: 1200px; height: 1000px; overflow: hidden;
    background: var(--page);
  }
  .ad {
    position: absolute; left: 167px; top: 22px;
    width: 866px; height: 953px;
    background: var(--ad-bg);
    overflow: hidden;
    font-family: "Roboto Condensed", "Arial Narrow", sans-serif;
    color: var(--white);
  }
  .abs { position: absolute; white-space: nowrap; }

  .hero-photo {
    position: absolute; left: 0; top: 110px;
    width: 440px; height: 558px;
    background:
      radial-gradient(ellipse at 30% 45%, var(--photo-light) 0%, var(--photo-mid) 40%, transparent 75%),
      radial-gradient(ellipse at 75% 80%, #3c5a44 0%, transparent 60%),
      linear-gradient(180deg, var(--ad-bg) 0%, var(--photo-dark) 60%, var(--ad-bg) 100%);
  }

  .headline, .topic { font-family: "Archivo Black", "Arial Black", sans-serif; }
  .headline { left: 336px; top: 30px; font-size: 58px; line-height: 1; }
  .topic { color: var(--gold); line-height: 1; }
  .topic--trusts { left: 473px; top: 112px; font-size: 86px; }
  .topic--annuities { left: 476px; top: 200px; font-size: 34px; }
  .topic--long-term { left: 476px; top: 249px; font-size: 34px; }
  .topic--care { left: 567px; top: 288px; font-size: 78px; }

  .question-mark {
    left: 340px; top: 372px;
    font-family: "Roboto Condensed", sans-serif; font-weight: 700;
    font-size: 380px; line-height: 1; color: var(--white);
  }

  .questions { list-style: none; }
  .questions li {
    position: absolute; white-space: nowrap;
    font-weight: 700; font-size: 14px; line-height: 1;
  }

  .cta { left: 20px; top: 700px; font-weight: 700; font-size: 29px; color: var(--cream); }

  .brand {
    position: absolute; left: 48px; top: 845px;
    display: flex; align-items: center; gap: 10px;
  }
  .brand__dot { width: 14px; height: 14px; border-radius: 50%; background: var(--gold); }
  .brand__name { font-weight: 700; font-size: 22px; color: var(--gold); }

  .presenter { left: 327px; top: 750px; }
  .presenter__label { font-weight: 700; font-size: 15px; }
  .presenter__name { font-weight: 700; font-size: 17px; color: var(--gold); margin-top: 2px; }
  .presenter__line { font-weight: 700; font-size: 10px; line-height: 13px; }

  .workshop {
    position: absolute; left: 320px; top: 842px;
    width: 238px; height: 98px;
    border: 1px solid #bdb8b2;
  }
  .workshop__label {
    position: absolute; left: 6px; top: -8px;
    padding: 0 3px; background: var(--ad-bg);
    font-weight: 700; font-size: 11px; color: var(--cream);
  }
  .workshop__text {
    position: absolute; left: 9px; top: 12px;
    font-weight: 700; font-size: 11px; line-height: 13px; white-space: nowrap;
  }
  .workshop__gap { height: 11px; }

  .tagline { left: 601px; top: 770px; font-weight: 700; font-size: 21px; color: var(--gold); }
  .tagline-sub { left: 601px; top: 801px; font-weight: 700; font-size: 11px; color: var(--gold); }
  .rsvp { left: 601px; top: 838px; font-weight: 700; font-size: 21px; line-height: 25px; }
  .slogan { left: 601px; top: 907px; font-weight: 700; font-style: italic; font-size: 18px; color: var(--cream); }
</style>
</head>
<body>
<main class="ad">
  <div class="hero-photo" role="img" aria-label="Photo of a large stack of hundred dollar bills with a businessman pushing against it"></div>

  <h1 class="abs headline">New Tax Laws</h1>
  <div class="abs topic topic--trusts">Trusts</div>
  <div class="abs topic topic--annuities">Annuities</div>
  <div class="abs topic topic--long-term">and Long Term</div>
  <div class="abs topic topic--care">Care</div>

  <div class="abs question-mark" aria-hidden="true">?</div>

  <ul class="questions">
    <li style="left:503px;top:396px">Is my living Trust right for me?</li>
    <li style="left:520px;top:420px">Does my existing Trust need to be changed?</li>
    <li style="left:527px;top:443px">Why does Joint Tenancy create tax problems?</li>
    <li style="left:530px;top:467px">I have a will, isn’t that enough?</li>
    <li style="left:532px;top:491px">Why do I need powers of attorney?</li>
    <li style="left:525px;top:515px">How much are inheritance taxes?</li>
    <li style="left:510px;top:539px">What are the new Affordable Care Act Taxes?</li>
    <li style="left:488px;top:563px">How does Long Term Care insurance work?</li>
    <li style="left:468px;top:587px">The average cost of long term care is over 80K a year-</li>
    <li style="left:468px;top:611px">how do I plan for those costs?</li>
    <li style="left:470px;top:635px">The truth about annuities-</li>
    <li style="left:467px;top:659px">What are the biggest mistakes in estate planning?</li>
  </ul>

  <div class="abs cta">Come learn what you need to know</div>

  <div class="brand">
    <span class="brand__dot"></span>
    <span class="brand__name">Whitfield Law</span>
  </div>

  <div class="abs presenter">
    <div class="presenter__label">Presented by:</div>
    <div class="presenter__name">dana marie whitfield</div>
    <div class="presenter__line">Attorney at Law</div>
    <div class="presenter__line">2146 Harbor Lane, Soquel.</div>
  </div>

  <section class="workshop">
    <span class="workshop__label">Workshop Time / Place</span>
    <div class="workshop__text">
      September 19, 2013, 1-2:30pm,&nbsp;&nbsp; 6-7:30pm
      <div class="workshop__gap"></div>
      Coastline Garden Inn, Aptos<br>
      4200 Cypress View Court<br>
      Aptos, California 95003
    </div>
  </section>

  <div class="abs tagline">Helping&nbsp; Families</div>
  <div class="abs tagline-sub">plan their estates for over 20 years.</div>
  <div class="abs rsvp">RSVP seating is limited:<br>(831) 555 - 0142</div>
  <div class="abs slogan">Be Smart. Plan Ahead.</div>
</main>
</body>
</html>
```